Fine Art business needs new website

We need a simple website with a home page, about us page, New sculptures, Sold sculptures, and a contact us page.Our sculptures are very high end one of a kind pieces. As such we need the site to be VERY elegant and professional. Lastly, because I'll be updating pictures on the website on a monthly basis it needs to be user friendly to update (Wordpress is preferred). The only branding we have so far for the business is a business card.
Updates
I wasn't completely ready when this project launched, also I am on the road right now and haven't been able to be as responsive to all you designers as I would like. I will work on giving feedback to all the top designs we've received so far. Thank you all so much for your participation and hardwork.
Target Market(s)
High end customers (affluent), art collectors, interior decorators/designers
Industry/Entity Type
Art Gallery
Coding
Coded - Design and coding required
Number of Pages Required
5+ page
Requirements
Must have
- Easily editable picture gallery for myself so that I can add new pieces(pictures of the pieces), remove sold pieces, etc. I would like the website to be built in wordpress so I can update it. I currently use sitekeeperpro through Netbirch for my other business website and would like to do the same for this one.
- Pages:
- -Intro page with featured pieces
- -Current pieces gallery (for sale) mainly a picture gallery
- -Sculptures archive (sold pieces) another picture gallery
- -About us: Pull-down of -about the artist (attached content)
- -Artistic Process (attached content)
- -Show Schedule:
- -one page dedicated to "friends of QMW" (basically a link page)
- TO BE CLEAR "www.lanternhollow.com" IS A TOTALLY DIFFERENT SITE AND I'M NOT TRYING TO COMBINE THE TWO OR JOIN THEM INTO ONE. This page needs be more elegant and seperate from the Lantern Hollow site.
- UPDATE: I'd like a link to the QMW Facebook page: https://www.facebook.com/quillmarkworks/
Nice to have
- I would like the pictures on the gallery pages able to have text connected with them (Materials, price)
- I would like the site style and fonts to be similar to our business cards we've already had designed (picture attached).
Should not have
- Too much flash or other things that will make the site slow to load.

```html
<!DOCTYPE html>
<html lang="en">
<head>
<meta charset="utf-8">
<title>Quill Mark Works</title>
<link rel="stylesheet" href="https://fonts.googleapis.com/css2?family=Playfair+Display:wght@400&family=Cinzel:wght@400&family=Poppins:wght@400;500&family=Roboto:wght@400;500&display=swap">
<style>
:root{
  --purple:#4b3b98;
  --purple-dark:#35286f;
  --band:#2a1c5c;
  --ink:#1d1d1d;
  --text:#444;
  --light:#eeeeee;
  --footer:#121212;
  --footer-text:#dddddd;
  --white:#fff;
}
*{box-sizing:border-box;margin:0;padding:0}
html,body{width:1200px;height:4045px;overflow:hidden}
body{position:relative;background:var(--white);font-family:"Roboto",sans-serif;color:var(--text)}
.abs{position:absolute}
.btn{position:absolute;display:flex;align-items:center;justify-content:center;background:var(--purple-dark);color:var(--white);font:500 19px "Roboto",sans-serif;text-decoration:none}
.section-title{position:absolute;left:0;width:1200px;text-align:center;font:500 45px "Poppins",sans-serif;color:var(--ink)}
.section-title::after{content:"";display:block;width:86px;height:3px;background:var(--purple);margin:14px auto 0}
.section-title.on-dark{color:var(--white)}
.section-title.on-dark::after{background:var(--white)}
.para{font-size:14px;line-height:31px;color:#333}
.photo{position:absolute}

/* nav */
.topbar{left:0;top:0;width:1200px;height:90px;background:var(--purple)}
.brand{left:0;top:0;width:445px;height:90px;background:var(--white);display:flex;align-items:center;padding-left:92px;font:400 27px "Cinzel",serif;letter-spacing:2px;color:#222}
.menu{left:485px;top:0;height:90px;display:flex;align-items:center;gap:30px;list-style:none}
.menu a{color:var(--white);font:400 17px "Playfair Display",serif;text-decoration:none;white-space:nowrap}
.search{left:1088px;top:35px}

/* hero */
.hero{left:0;top:90px;width:1200px;height:553px;background:radial-gradient(ellipse at 70% 50%,#2a2a2a,#0e0e0e 70%)}
.hero-title{left:115px;top:205px;font:400 96px/90px "Playfair Display",serif;color:var(--white)}
.hero-sub{left:117px;top:402px;font:400 29px "Roboto",sans-serif;color:var(--white)}

/* about */
.about-accent{left:92px;top:734px;width:440px;height:300px}
.about-label{left:610px;top:768px;font:400 28px "Poppins",sans-serif;color:var(--ink)}
.about-title{left:610px;top:796px;font:500 44px "Poppins",sans-serif;color:var(--ink)}
.about-rule{left:612px;top:863px;width:118px;height:3px;background:var(--purple)}

/* products */
.products{left:0;top:1220px;width:1200px;height:705px;background:var(--light)}
.product-name{position:absolute;width:235px;text-align:center;font:400 24px "Roboto",sans-serif;color:#222}
.product-price{position:absolute;width:235px;text-align:center;font:400 20px "Roboto",sans-serif;color:var(--purple)}
.arrow-circle{position:absolute;width:40px;height:40px;border-radius:50%;background:var(--white);display:flex;align-items:center;justify-content:center;box-shadow:0 1px 3px rgba(0,0,0,.15)}

/* testimonials */
.testimonials{left:0;top:2380px;width:1200px;height:438px;background:radial-gradient(ellipse at 50% 40%,#3a2a78,var(--band) 75%)}
.quote{position:absolute;left:0;top:2604px;width:1200px;text-align:center;color:var(--white);font:400 15px/31px "Roboto",sans-serif}
.author{position:absolute;left:0;top:2716px;width:1200px;text-align:center;color:var(--white);font:400 19px "Roboto",sans-serif}

/* footer */
.footer{left:0;top:3610px;width:1200px;height:435px;background:var(--footer)}
.f-head{position:absolute;font:400 20px "Roboto",sans-serif;color:var(--white)}
.f-item{position:absolute;font-size:14px;color:var(--footer-text);display:flex;align-items:flex-start;gap:20px}
.f-links{position:absolute;list-style:none;font-size:14px;color:var(--footer-text)}
.f-links li{height:26px;padding-left:18px;position:relative}
.f-links li::before{content:"";position:absolute;left:0;top:7px;width:5px;height:5px;border-radius:50%;background:var(--footer-text)}
.f-social{position:absolute;list-style:none;font-size:16px;color:var(--footer-text)}
.f-social li{height:40px;display:flex;align-items:center;gap:12px}
.f-social li span{width:26px;height:26px;border:1.5px solid var(--footer-text);border-radius:50%}
.copy{left:0;top:3978px;width:1200px;text-align:center;font-size:14px;color:var(--footer-text)}
</style>
</head>
<body>

<header>
  <div class="abs topbar"></div>
  <div class="abs brand">QUILL MARK WORKS</div>
  <ul class="abs menu">
    <li><a href="#">Home</a></li>
    <li><a href="#">About us</a></li>
    <li><a href="#">New sculptures</a></li>
    <li><a href="#">Sold sculptures</a></li>
    <li><a href="#">Contact us</a></li>
  </ul>
  <svg class="abs search" width="20" height="20" viewBox="0 0 20 20" aria-label="Search"><circle cx="8" cy="8" r="6" fill="none" stroke="#fff" stroke-width="2.5"/><line x1="12.5" y1="12.5" x2="18" y2="18" stroke="#fff" stroke-width="3"/></svg>
</header>

<section class="hero-block">
  <div class="abs hero"></div>
  <div class="photo" role="img" aria-label="Polished stone spiral sculpture on a dark pedestal" style="left:620px;top:100px;width:560px;height:543px;background:radial-gradient(ellipse at 45% 40%,#8a6a3a,#4a3520 40%,rgba(20,15,10,0) 70%)"></div>
  <h1 class="abs hero-title">Quill Mark<br>Works</h1>
  <p class="abs hero-sub">It is a long established fact that</p>
  <a class="btn" href="#" style="left:117px;top:467px;width:142px;height:46px">View More</a>
</section>

<section class="about">
  <svg class="abs about-accent" viewBox="0 0 440 300"><polygon points="0,0 440,0 440,22 22,300 0,300" fill="#35286f"/></svg>
  <div class="photo" role="img" aria-label="Video still of two halves of a cut white geode" style="left:117px;top:758px;width:444px;height:329px;background:linear-gradient(135deg,#3a3a3a,#b9b6b0 40%,#e6e3de 55%,#6d6a66);box-shadow:0 4px 12px rgba(0,0,0,.35)"></div>
  <svg class="abs" style="left:305px;top:888px" width="68" height="68" viewBox="0 0 68 68" aria-label="Play video"><circle cx="34" cy="34" r="32" fill="rgba(40,40,40,.75)"/><polygon points="27,20 50,34 27,48" fill="#fff"/></svg>
  <p class="abs about-label">About</p>
  <h2 class="abs about-title">Quill Mark Works</h2>
  <div class="abs about-rule"></div>
  <p class="abs para" style="left:610px;top:876px;width:500px">The point of using Lorem Ipsum is that it has a more-or-less normal distribution of letters, as opposed to using 'Content here, content here', making it look like readable English. Many desktop publishing packages and web page editors now use Lorem Ipsum as their default model text, and a search for 'lorem ipsum' will uncover many web sites still in their infancy.</p>
  <a class="btn" href="#" style="left:610px;top:1036px;width:126px;height:36px;font-size:17px">Read More</a>
  <div class="photo" role="img" aria-label="Amethyst crystal cluster" style="left:796px;top:1090px;width:404px;height:130px;background:radial-gradient(ellipse at 55% 100%,#5a3a9a,#2c1a5a 45%,rgba(255,255,255,0) 70%)"></div>
</section>

<section class="product-block">
  <div class="abs products"></div>
  <h2 class="section-title" style="top:1315px">Our Product</h2>
  <div class="arrow-circle" style="left:47px;top:1560px"><svg width="12" height="18" viewBox="0 0 12 18"><polyline points="10,2 3,9 10,16" fill="none" stroke="#666" stroke-width="2"/></svg></div>
  <div class="arrow-circle" style="left:1113px;top:1560px"><svg width="12" height="18" viewBox="0 0 12 18"><polyline points="2,2 9,9 2,16" fill="none" stroke="#666" stroke-width="2"/></svg></div>

  <div class="photo" role="img" aria-label="Green malachite sculpture" style="left:100px;top:1435px;width:235px;height:313px;background:radial-gradient(ellipse at 50% 40%,#2f7a4f,#0c1a12 60%,#060606);box-shadow:0 2px 8px rgba(0,0,0,.3)"></div>
  <div class="photo" role="img" aria-label="Amber swirl sculpture" style="left:356px;top:1435px;width:235px;height:313px;background:radial-gradient(ellipse at 50% 40%,#a06a2a,#241508 60%,#060606);box-shadow:0 2px 8px rgba(0,0,0,.3)"></div>
  <div class="photo" role="img" aria-label="Blue agate slab sculpture" style="left:612px;top:1435px;width:235px;height:313px;background:radial-gradient(ellipse at 50% 40%,#7a8aa0,#1a1e26 60%,#060606);box-shadow:0 2px 8px rgba(0,0,0,.3)"></div>
  <div class="photo" role="img" aria-label="Glowing ammonite sculpture" style="left:868px;top:1435px;width:235px;height:313px;background:radial-gradient(ellipse at 50% 40%,#d07a20,#3a1a06 60%,#060606);box-shadow:0 2px 8px rgba(0,0,0,.3)"></div>

  <p class="product-name" style="left:100px;top:1762px">Porro quisquam</p>
  <p class="product-price" style="left:100px;top:1800px">$59.00</p>
  <p class="product-name" style="left:356px;top:1762px">Dolorem ipsum</p>
  <p class="product-price" style="left:356px;top:1800px">$59.00</p>
  <p class="product-name" style="left:612px;top:1762px">Neque porro</p>
  <p class="product-price" style="left:612px;top:1800px">$59.00</p>
  <p class="product-name" style="left:868px;top:1762px">Ipsum quia</p>
  <p class="product-price" style="left:868px;top:1800px">$59.00</p>
</section>

<section class="what-we-do">
  <h2 class="abs" style="left:92px;top:1995px;font:500 44px 'Poppins',sans-serif;color:var(--ink)">What We Do</h2>
  <div class="abs" style="left:94px;top:2058px;width:110px;height:3px;background:var(--purple)"></div>
  <p class="abs para" style="left:92px;top:2074px;width:510px">The point of using Lorem Ipsum is that it has a more-or-less normal distribution of letters, as opposed to using 'Content here, content here', making it look like readable English. Many desktop publishing packages and web page editors now use Lorem Ipsum as their default model text, and a search for 'lorem ipsum' will uncover many web sites still in their infancy.</p>
  <a class="btn" href="#" style="left:92px;top:2236px;width:126px;height:36px;font-size:17px">Read More</a>
  <div class="photo" role="img" aria-label="Large amethyst geode cluster" style="left:647px;top:1970px;width:553px;height:350px;background:radial-gradient(ellipse at 55% 55%,#7a5ab8,#3c237a 40%,rgba(255,255,255,0) 70%)"></div>
</section>

<section class="testimonial-block">
  <div class="abs testimonials"></div>
  <h2 class="section-title on-dark" style="top:2440px">Testimonials</h2>
  <svg class="abs" style="left:577px;top:2552px" width="46" height="38" viewBox="0 0 46 38" aria-hidden="true"><path d="M4 38V22C4 10 10 3 20 0l2 5C15 8 13 13 13 18h7v20zM27 38V22C27 10 33 3 43 0l2 5c-7 3-9 8-9 13h7v20z" fill="#fff"/></svg>
  <p class="quote">I went to the Lantern Hollow booth at the 2016 renaissance fair in Colorado today, and can honestly say, I was highly satisfied<br>with my geode. It was a bit stubborn while trying to crack it open, but what I saw inside surprised me. It looked like snow, but<br>it was more beautiful then snow that I've seen fall since I've been in Colorado</p>
  <p class="author">-Odelia R</p>
  <svg class="abs" style="left:72px;top:2612px" width="20" height="36" viewBox="0 0 20 36"><polyline points="18,2 3,18 18,34" fill="none" stroke="#fff" stroke-width="2.5"/></svg>
  <svg class="abs" style="left:1108px;top:2612px" width="20" height="36" viewBox="0 0 20 36"><polyline points="2,2 17,18 2,34" fill="none" stroke="#fff" stroke-width="2.5"/></svg>
</section>

<section class="gallery">
  <h2 class="section-title" style="top:2905px">Our Gallery</h2>
  <div class="photo" role="img" aria-label="White quartz geode" style="left:92px;top:3023px;width:245px;height:200px;background:radial-gradient(ellipse at 50% 55%,#e8e4dc,#6a5a4a 55%,#2a2018)"></div>
  <div class="photo" role="img" aria-label="Rough brown geode" style="left:347px;top:3023px;width:245px;height:200px;background:radial-gradient(ellipse at 50% 50%,#b06a35,#3a1e0e 55%,#0a0a0a)"></div>
  <div class="photo" role="img" aria-label="Golden septarian slab" style="left:602px;top:3023px;width:245px;height:200px;background:radial-gradient(ellipse at 50% 50%,#c9a55a,#5a4220 55%,#111)"></div>
  <div class="photo" role="img" aria-label="Dark crystal geode half" style="left:857px;top:3023px;width:249px;height:200px;background:radial-gradient(ellipse at 50% 50%,#6a5a6a,#d8d0c8 40%,#2a2420 70%)"></div>
  <div class="photo" role="img" aria-label="Banded agate heart" style="left:92px;top:3233px;width:245px;height:200px;background:radial-gradient(ellipse at 50% 50%,#f2f0ec,#8a6a50 50%,#1e1a18)"></div>
  <div class="photo" role="img" aria-label="Stone spiral sculpture" style="left:347px;top:3233px;width:245px;height:200px;background:radial-gradient(ellipse at 50% 45%,#8a6a3a,#2a1e10 55%,#0a0a0a)"></div>
  <div class="photo" role="img" aria-label="Purple crystal slab" style="left:602px;top:3233px;width:245px;height:200px;background:radial-gradient(ellipse at 50% 50%,#5a3aa0,#1e1240 55%,#0a0a0a)"></div>
  <div class="photo" role="img" aria-label="Rough brown mineral specimen" style="left:857px;top:3233px;width:249px;height:200px;background:radial-gradient(ellipse at 50% 50%,#7a5040,#2a1a14 55%,#0a0a0a)"></div>
  <div class="photo" role="img" aria-label="Amethyst crystal cluster" style="left:690px;top:3500px;width:450px;height:110px;background:radial-gradient(ellipse at 50% 100%,#5a3a9a,#2c1a5a 45%,rgba(255,255,255,0) 72%)"></div>
</section>

<footer>
  <div class="abs footer"></div>
  <div class="photo" role="img" aria-label="Amethyst crystal" style="left:92px;top:3722px;width:272px;height:110px;background:radial-gradient(ellipse at 50% 60%,#6a4aa8,#2e1c60 50%,rgba(18,18,18,0) 72%)"></div>
  <p class="abs" style="left:92px;top:3835px;width:272px;text-align:center;font:400 13px 'Cinzel',serif;letter-spacing:1.5px;color:var(--footer-text)">QUILL MARK WORKS</p>

  <h3 class="f-head" style="left:475px;top:3695px">CONTACT US</h3>
  <div class="f-item" style="left:477px;top:3750px;width:250px">
    <svg width="14" height="18" viewBox="0 0 14 18"><path d="M7 0a7 7 0 0 0-7 7c0 5 7 11 7 11s7-6 7-11a7 7 0 0 0-7-7z" fill="#fff"/><circle cx="7" cy="7" r="2.5" fill="#121212"/></svg>
    <span style="line-height:20px">14, Wren Court, Ashmere,<br>WA 6021</span>
  </div>
  <div class="f-item" style="left:477px;top:3815px">
    <svg width="14" height="14" viewBox="0 0 14 14"><path d="M3 0l3 3-2 2c1 2 3 4 5 5l2-2 3 3-2 3C6 14 0 8 0 2z" fill="#fff"/></svg>
    <span>(970)555-0142</span>
  </div>
  <div class="f-item" style="left:477px;top:3854px">
    <svg width="16" height="12" viewBox="0 0 16 12"><rect width="16" height="12" fill="#fff"/><polyline points="0,0 8,7 16,0" fill="none" stroke="#121212" stroke-width="1.5"/></svg>
    <span>mara@lanternhollow.com</span>
  </div>

  <h3 class="f-head" style="left:769px;top:3695px">QUICK LINKS</h3>
  <ul class="f-links" style="left:772px;top:3748px">
    <li>Home</li><li>About us</li><li>Product</li><li>Services</li><li>Contact Us</li>
  </ul>

  <h3 class="f-head" style="left:987px;top:3695px">FOLLOW US</h3>
  <ul class="f-social" style="left:990px;top:3747px">
    <li><span></span>Facebook</li><li><span></span>Twitter</li><li><span></span>Google+</li><li><span></span>youtube</li>
  </ul>

  <p class="abs copy">© Copyright 2018 . All Rights Reserved.</p>
</footer>

</body>
</html>
```